M&A Advisory firm needs elegant and powerful letterhead

We need a powerful but elegant letterhead to engage with the international financial industry.

Target Market(s)

New York and International Financial Industry

Industry/Entity Type

Finance

Font styles to use
Other font styles liked:
• Poppins

Requirements
Must have
• 482 W 71st Street 14th Floor New York, NY 10157 O: +1 (212) 555 0147 F: +1 (212) 555 0182

```html
<!DOCTYPE html>
<html lang="en">
<head>
<meta charset="utf-8">
<title>Meridale Letterhead</title>
<link href="https://fonts.googleapis.com/css2?family=Poppins:wght@400;500;600&display=swap" rel="stylesheet">
<style>
  :root {
    --navy: #0d3f8c;
    --ink: #151515;
    --body-grey: #5a5a5a;
    --paper: #eeeef0;
    --rule-grey: #7d7d80;
    --sig-tone: #c9d2e3;
  }
  * { margin: 0; padding: 0; box-sizing: border-box; }
  html, body { width: 944px; height: 1200px; overflow: hidden; background: var(--paper); }
  .letterhead {
    position: relative; width: 944px; height: 1200px;
    background: var(--paper);
    font-family: "Poppins", sans-serif;
  }
  .brand {
    position: absolute; left: 101px; top: 72px;
    display: flex; align-items: center; gap: 16px;
  }
  .brand-dot { width: 42px; height: 42px; border-radius: 50%; background: var(--navy); }
  .brand-name {
    font-size: 58px; font-weight: 500; color: var(--navy);
    letter-spacing: 1px; line-height: 1;
  }
  .margin-rule {
    position: absolute; left: 79px; top: 206px;
    width: 4px; height: 792px; background: var(--navy);
  }
  .recipient { position: absolute; left: 99px; top: 212px; color: var(--ink); }
  .recipient-label { font-size: 28px; font-weight: 500; line-height: 1.1; }
  .recipient-name { font-size: 30px; font-weight: 600; line-height: 1.15; }
  .letter-body {
    position: absolute; left: 99px; top: 322px; width: 740px;
    font-size: 14px; line-height: 23px; color: var(--body-grey);
  }
  .letter-body p + p { margin-top: 22px; }
  .signature {
    position: absolute; left: 95px; top: 840px;
    width: 215px; height: 105px; border-radius: 6px;
    background: linear-gradient(120deg, var(--sig-tone), #dfe4ee);
  }
  .footer { position: absolute; left: 0; top: 1148px; width: 944px; height: 52px; }
  .footer svg { position: absolute; inset: 0; }
  .contact-line {
    position: absolute; left: 60px; top: 10px;
    font-size: 16px; font-weight: 600; color: var(--ink);
  }
  .contact-line span + span { margin-left: 14px; }
  .address {
    position: absolute; left: 511px; top: 15px;
    font-size: 17px; font-weight: 500; color: #fff;
  }
</style>
</head>
<body>
<main class="letterhead">
  <header class="brand">
    <span class="brand-dot"></span>
    <span class="brand-name">MERIDALE</span>
  </header>

  <div class="margin-rule"></div>

  <section class="recipient">
    <div class="recipient-label">To</div>
    <div class="recipient-name">ELLIS MORGAN</div>
  </section>

  <article class="letter-body">
    <p>Lorem ipsum dolor sit amet, consectetur adipiscing elit, sed do eiusmod tempor incididunt ut labore et dolore magna aliqua. Ut enim ad minim veniam, quis nostrud exercitation ullamco laboris nisi ut aliquip ex ea commodo consequat. Duis aute irure dolor in reprehenderit in voluptate velit esse cillum dolore eu fugiat nulla pariatur. Excepteur sint occaecat cupidatat non proident, sunt in culpa qui officia deserunt mollit anim id est laborum.</p>
    <p>ed ut perspiciatis unde omnis iste natus error sit voluptatem accusantium doloremque laudantium, totam rem aperiam, eaque ipsa quae ab illo inventore veritatis et quasi architecto beatae vitae dict a sunt explicabo. Nemo enim ipsam voluptatem quia voluptas sit aspernatur aut odit aut fugit ,sed quia consequuntur magni dolores eos qui ratione voluptatem</p>
    <p>sequi nesciunt. Neque porro quisquam est, qui dolorem ipsum quia dolor sit amet, consectetur, adipisci velit, sed quia non numquam eius modi tempora incidunt ut labore et dolore magnam aliquam quaerat voluptatem.</p>
    <p>Ut enim ad minima veniam, quis nostrum exercitationem ullam corporis suscipit laboriosam, nisi ut aliquid ex ea commodi consequatur? Quis autem vel eum iure reprehenderit qui in ea voluptate velit esse quam nihil molestiae consequatur, vel illum qui dolorem eum fugiat quo voluptas nulla pariatur</p>
  </article>

  <div class="signature" role="img" aria-label="Handwritten signature of the sender"></div>

  <footer class="footer">
    <svg width="944" height="52" viewBox="0 0 944 52" aria-hidden="true">
      <rect x="0" y="35" width="440" height="3" fill="var(--rule-grey)"/>
      <path d="M420 40 C455 40 465 0 500 0 L944 0 L944 52 L420 52 Z" fill="var(--navy)"/>
      <rect x="0" y="40" width="944" height="12" fill="var(--navy)"/>
    </svg>
    <div class="contact-line"><span>O: +1 (212) 555 0147</span><span>F: +1 (212) 555 0182</span></div>
    <div class="address">482 W 71st Street 14th Floor New York, NY 10157</div>
  </footer>
</main>
</body>
</html>
```